BRIM Outreach Partners Business Card Rebrand

Hello Designers! We are looking for help designing our new business card to go in conjunction with our company rebrand. Unfortunately, we have an event mid June that requires we get these printed ASAP (before our new website is launched.) We have a mostly complete Brand Book which I have uploaded to this request for your reference to company information, style, fonts. I've also enclosed our logo file in .eps & .jpg. Attached is a sample business card my boss liked but said was "too simple." I made it in Canva and do not profess to be a designer. NOT FOR DESIGN REFERENCE, ONLY FOR CONTEXT Here is what our old website looks like: https://brimoutreachpartners.com/.

```html
<!DOCTYPE html>
<html lang="en">
<head>
<meta charset="utf-8">
<title>BRIM Outreach Partners – Business Card</title>
<link href="https://fonts.googleapis.com/css2?family=Poppins:wght@600&family=Arimo:wght@400&display=swap" rel="stylesheet">
<style>
  :root {
    --brand-blue: #4db3e4;
    --ink: #111111;
    --paper: #ffffff;
    --backdrop: #ecedef;
  }
  * { margin: 0; padding: 0; box-sizing: border-box; }
  html, body { width: 1200px; height: 1000px; overflow: hidden; background: var(--backdrop); }
  .canvas { position: relative; width: 1200px; height: 1000px; }

  .card { position: absolute; left: 303px; width: 593px; height: 338px; background: var(--paper); overflow: hidden; }
  .card--front { top: 108px; }
  .card--back { top: 553px; }

  .card__top-band { position: absolute; left: 0; top: 0; width: 100%; height: 8px; background: var(--brand-blue); }

  .brand { position: absolute; display: flex; align-items: center; }
  .brand__dot { border-radius: 50%; flex: none; }
  .brand__name { font-family: 'Poppins', sans-serif; font-weight: 600; color: var(--ink); line-height: 1.08; }

  .card--front .brand { left: 334px; top: 42px; gap: 12px; }
  .card--front .brand__dot { width: 74px; height: 74px; background: var(--brand-blue); }
  .card--front .brand__name { font-size: 21px; width: 165px; }

  .person { position: absolute; left: 43px; top: 144px; }
  .person__name { font-family: 'Poppins', sans-serif; font-weight: 600; font-size: 24.5px; color: var(--brand-blue); line-height: 1.2; white-space: nowrap; }
  .person__title { font-family: 'Arimo', sans-serif; font-size: 14px; color: var(--ink); margin-top: 5px; letter-spacing: 0.2px; }

  .divider { position: absolute; left: 0; top: 219px; width: 296px; height: 2px; background: var(--brand-blue); }

  .contact { position: absolute; left: 43px; top: 236px; list-style: none; font-family: 'Arimo', sans-serif; font-size: 13.5px; color: var(--ink); white-space: nowrap; }
  .contact li { height: 23.5px; }

  .website { position: absolute; right: 42px; top: 279px; font-family: 'Arimo', sans-serif; font-size: 15.5px; color: var(--ink); white-space: nowrap; }

  .card--back { background: var(--brand-blue); }
  .card__top-strip { position: absolute; left: 0; top: 0; width: 100%; height: 8px; background: var(--paper); }
  .card--back .brand { left: 128px; top: 111px; gap: 20px; }
  .card--back .brand__dot { width: 114px; height: 114px; background: var(--paper); }
  .card--back .brand__name { font-size: 36px; width: 300px; }
</style>
</head>
<body>
<main class="canvas">
  <section class="card card--front">
    <div class="card__top-band"></div>
    <div class="brand">
      <span class="brand__dot"></span>
      <span class="brand__name">BRIM Outreach Partners</span>
    </div>
    <div class="person">
      <h1 class="person__name">Daniel Rourke-Hale</h1>
      <p class="person__title">MANAGING PARTNER</p>
    </div>
    <div class="divider"></div>
    <ul class="contact">
      <li>+1-404-555-0172</li>
      <li>Savannah, GA office (Eastern Time)</li>
      <li>daniel@brimoutreachpartners.com</li>
    </ul>
    <p class="website">www.brimoutreachpartners.com</p>
  </section>

  <section class="card card--back">
    <div class="card__top-strip"></div>
    <div class="brand">
      <span class="brand__dot"></span>
      <span class="brand__name">BRIM Outreach Partners</span>
    </div>
  </section>
</main>
</body>
</html>
```